Redesign of Grantlyhub.com

We need a redesign of some key-pages on our crowdfunding website for mobile apps, GrantlyHub.com.

- Redesign of homepage
http://www.grantlyhub.com/en

- Redesign of project submission page
http://www.grantlyhub.com/en/submit-your-app/submit-your-app

- Redesign of browsing section
http://www.grantlyhub.com/en/fund-apps

- Redesign of project funding page
http://www.grantlyhub.com/en/fund-apps/sponsor/sketch-riddler?amount=5.00

Design should be highly focused on a great user experience for users of the platform, being in principal mobile developers. So we need a great user experience for mobile developers using our service.

Benchmark designs we particularly like are:
http://www.pledgorama.com/
http://www.tradebitly.com/landing/
http://www.vomba.com/

Design should have a more 'fun, happy to get involved' factor as it has nox.
Updates

Logo's have been uploaded

Target Market(s)

mobile app developers

Industry/Entity Type

Crowdfunding

Requirements
Must have
• Submission forms must have explanation fields next to the form

Homepage should have design in whihc a introductary video can be integrated

```html
<!DOCTYPE html>
<html lang="en">
<head>
<meta charset="utf-8">
<title>GrantlyHub – Most funded and our picks</title>
<link href="https://fonts.googleapis.com/css2?family=Cabin:wght@400;600;700&display=swap" rel="stylesheet">
<style>
  :root {
    --page-bg: #ffffff;
    --band-bg: #ebebeb;
    --card-bg: #ffffff;
    --text-main: #4a4a4a;
    --text-strong: #333333;
    --accent-green: #9ac31c;
    --accent-green-dark: #7fa313;
    --pill-blue: #3b7db3;
    --shadow: rgba(0, 0, 0, 0.14);
  }
  * { box-sizing: border-box; margin: 0; padding: 0; }
  html, body { width: 1200px; height: 483px; overflow: hidden; background: var(--page-bg); }
  body { font-family: "Cabin", "Gill Sans", sans-serif; color: var(--text-main); position: relative; }

  .bottom-band { position: absolute; left: 0; top: 442px; width: 1200px; height: 41px; background: var(--band-bg); }

  .showcase-card {
    position: absolute; left: 0; top: 41px; width: 1185px; height: 390px;
    background: var(--card-bg);
    box-shadow: 0 6px 14px var(--shadow);
  }

  .section-heading {
    position: absolute; top: 92px; display: flex; align-items: center;
    font-size: 48px; font-weight: 400; color: var(--text-main); letter-spacing: 0.2px;
  }
  .section-heading svg { display: block; }
  .heading-funded { left: 33px; }
  .heading-funded .heading-label { margin-left: 33px; }
  .heading-picks { left: 645px; }
  .heading-picks .heading-label { margin-left: 28px; }

  .app-tile { position: absolute; top: 208px; width: 170px; text-align: center; }
  .app-icon {
    width: 119px; height: 119px; margin: 0 auto; border-radius: 4px;
  }
  .app-name { margin-top: 18px; font-size: 22px; color: var(--text-strong); white-space: nowrap; }
  .app-funding { margin-top: 9px; font-size: 19px; color: var(--text-strong); display: flex; justify-content: center; align-items: center; gap: 5px; }
  .funding-pill {
    display: inline-block; background: var(--pill-blue); color: #fff;
    font-size: 16px; font-weight: 700; padding: 2px 9px; border-radius: 12px; line-height: 20px;
  }

  .icon-sketch { background: linear-gradient(180deg, #2a2a2a 0%, #3a3a3a 62%, #b0672e 62%, #8a4a1e 100%); }
  .icon-motif { background: linear-gradient(180deg, #c8211f 0%, #a8120f 100%); }
  .icon-zintaro { background: linear-gradient(180deg, #5c5c5c 0%, #3d3d3d 100%); }
  .icon-bolty { background: linear-gradient(160deg, #e0a23a 0%, #7a4a1c 100%); }
  .icon-gridiron { background: linear-gradient(180deg, #c9c3b8 0%, #6b5f52 100%); }
  .icon-deal { background: linear-gradient(180deg, #f4f4f4 0%, #e6e6e6 100%); }
</style>
</head>
<body>
  <div class="showcase-card"></div>
  <div class="bottom-band"></div>

  <h2 class="section-heading heading-funded">
    <svg width="44" height="78" viewBox="0 0 44 78" aria-hidden="true">
      <path d="M8 40 L2 74 L14 66 L20 78 L24 48 Z" fill="var(--accent-green)"/>
      <path d="M36 40 L42 74 L30 66 L24 78 L20 48 Z" fill="var(--accent-green-dark)"/>
      <circle cx="22" cy="24" r="22" fill="var(--accent-green)"/>
      <circle cx="22" cy="24" r="15" fill="#fff"/>
      <circle cx="22" cy="24" r="12" fill="var(--accent-green)"/>
      <path d="M22 15 L24.6 21 L31 21.4 L26 25.6 L27.6 32 L22 28.4 L16.4 32 L18 25.6 L13 21.4 L19.4 21 Z" fill="#fff"/>
    </svg>
    <span class="heading-label">Most funded</span>
  </h2>

  <h2 class="section-heading heading-picks">
    <svg width="72" height="58" viewBox="0 0 72 58" aria-hidden="true">
      <path d="M36 58 C20 44 0 32 0 16 C0 6 8 0 18 0 C26 0 32 5 36 11 C40 5 46 0 54 0 C64 0 72 6 72 16 C72 32 52 44 36 58 Z" fill="var(--accent-green)"/>
    </svg>
    <span class="heading-label">Our picks</span>
  </h2>

  <div class="app-tile" style="left:22px">
    <div class="app-icon icon-sketch" role="img" aria-label="App icon: chalkboard with a stick-figure drawing"></div>
    <p class="app-name">Sketch ridd...</p>
    <p class="app-funding">Funded: <span class="funding-pill">50%</span></p>
  </div>
  <div class="app-tile" style="left:200px">
    <div class="app-icon icon-motif" role="img" aria-label="App icon: cartoon bear on a red background"></div>
    <p class="app-name">MotifBear</p>
    <p class="app-funding">Funded: <span class="funding-pill">75%</span></p>
  </div>
  <div class="app-tile" style="left:374px">
    <div class="app-icon icon-zintaro" role="img" aria-label="App icon: orange letter with signal waves on grey"></div>
    <p class="app-name">Zintaro</p>
    <p class="app-funding">Funded: <span class="funding-pill">95%</span></p>
  </div>

  <div class="app-tile" style="left:634px">
    <div class="app-icon icon-bolty" role="img" aria-label="App icon: cartoon character in a golden frame"></div>
    <p class="app-name">Bolty Master</p>
    <p class="app-funding">Funded: <span class="funding-pill">15%</span></p>
  </div>
  <div class="app-tile" style="left:804px">
    <div class="app-icon icon-gridiron" role="img" aria-label="App icon: football helmet close-up"></div>
    <p class="app-name">Gridiron quiz</p>
    <p class="app-funding">Funded: <span class="funding-pill">45%</span></p>
  </div>
  <div class="app-tile" style="left:979px">
    <div class="app-icon icon-deal" role="img" aria-label="App icon: pink shopping cube with cart and euro sign"></div>
    <p class="app-name">Dealpocket</p>
    <p class="app-funding">Funded: <span class="funding-pill">10%</span></p>
  </div>
</body>
</html>
```